Accounting business needs a fridge magnet design

I need a business card size design to be used as a fridge magnet.
It will need to be vertical not horizontal and it will have my logo and the services I provide listed below it.
It needs to be pleasing to the eye and catch peoples attention.
I have uploaded my current business card as a reference.
It can look totally different though, i am open to new ideas.

It will need to say:

Specialising in:
*Small Business Taxation
*Company & Trust Returns
*Financial Statements
*Partnership Taxation
*BAS preparation/lodgement
*Capital Gains Tax
*Business Start Ups
*Business Structuring
*Tax Planning

```html
<!DOCTYPE html>
<html lang="en">
<head>
<meta charset="utf-8">
<title>Orbit Tax – Fridge Magnet</title>
<link rel="stylesheet" href="https://fonts.googleapis.com/css2?family=Montserrat:wght@500&family=Arimo:wght@400&display=swap">
<style>
  :root {
    --page-bg: #444444;
    --panel-dark: #27282b;
    --accent-blue: #16a6dd;
    --heading-blue: #1f5ea8;
    --card-white: #f3f3f4;
    --text-dark: #333436;
    --badge-blue: #1b59a2;
    --badge-sky: #1ab4e6;
    --line-black: #111111;
    --white: #ffffff;
  }
  * { margin: 0; padding: 0; box-sizing: border-box; }
  html, body {
    width: 1096px;
    height: 1200px;
    overflow: hidden;
    background: var(--page-bg);
  }
  .magnet {
    position: absolute;
    left: 284px;
    top: 140px;
    width: 527px;
    height: 921px;
    border-radius: 26px;
    overflow: hidden;
    background: var(--card-white);
  }
  .magnet-backdrop {
    position: absolute;
    inset: 0;
    width: 100%;
    height: 100%;
  }
  .brand-ring {
    position: absolute;
    left: 191px;
    top: 54px;
    width: 146px;
    height: 146px;
    border: 3.5px solid var(--white);
    border-radius: 50%;
  }
  .brand-name {
    position: absolute;
    left: 0;
    top: 240px;
    width: 100%;
    text-align: center;
    font-family: "Montserrat", sans-serif;
    font-weight: 500;
    font-size: 46px;
    letter-spacing: 0.32em;
    text-indent: 0.32em;
    color: var(--white);
  }
  .services-heading {
    position: absolute;
    left: 56px;
    top: 438px;
    font-family: "Arimo", sans-serif;
    font-weight: 400;
    font-size: 31px;
    color: var(--heading-blue);
  }
  .services-list {
    position: absolute;
    left: 61px;
    top: 491px;
    list-style: none;
    font-family: "Arimo", sans-serif;
    font-size: 23px;
    color: var(--text-dark);
  }
  .services-list li {
    display: flex;
    align-items: center;
    height: 33.7px;
  }
  .tick-icon {
    width: 20px;
    height: 20px;
    margin-right: 14px;
    flex: none;
  }
  .partner-badge {
    position: absolute;
    left: 59px;
    top: 827px;
    width: 138px;
    height: 59px;
    background: var(--badge-blue);
  }
  .partner-dot {
    position: absolute;
    left: 235px;
    top: 818px;
    width: 78px;
    height: 78px;
    border-radius: 50%;
    background: var(--badge-sky);
  }
</style>
</head>
<body>
  <div class="magnet">
    <svg class="magnet-backdrop" viewBox="0 0 457 798" preserveAspectRatio="none" aria-hidden="true">
      <rect x="0" y="0" width="457" height="420" fill="var(--panel-dark)"/>
      <path d="M0,311 C150,345 330,340 457,297 L457,420 L0,420 Z" fill="var(--accent-blue)"/>
      <path d="M0,318 C150,352 330,346 457,320" fill="none" stroke="var(--line-black)" stroke-width="1.4"/>
      <path d="M0,326 C120,362 330,366 457,327 L457,798 L0,798 Z" fill="var(--card-white)"/>
    </svg>

    <div class="brand-ring"></div>
    <div class="brand-name">ORBIT TAX</div>

    <h2 class="services-heading">Specialising in</h2>
    <ul class="services-list">
      <li><svg class="tick-icon" viewBox="0 0 20 20"><circle cx="9" cy="11" r="7" fill="none" stroke="var(--heading-blue)" stroke-width="2.2"/><path d="M5.5,10.5 L9,14 L18,4" fill="none" stroke="var(--heading-blue)" stroke-width="2.6" stroke-linecap="round" stroke-linejoin="round"/></svg>Small Business Taxation</li>
      <li><svg class="tick-icon" viewBox="0 0 20 20"><circle cx="9" cy="11" r="7" fill="none" stroke="var(--heading-blue)" stroke-width="2.2"/><path d="M5.5,10.5 L9,14 L18,4" fill="none" stroke="var(--heading-blue)" stroke-width="2.6" stroke-linecap="round" stroke-linejoin="round"/></svg>Company &amp; Trust Returns</li>
      <li><svg class="tick-icon" viewBox="0 0 20 20"><circle cx="9" cy="11" r="7" fill="none" stroke="var(--heading-blue)" stroke-width="2.2"/><path d="M5.5,10.5 L9,14 L18,4" fill="none" stroke="var(--heading-blue)" stroke-width="2.6" stroke-linecap="round" stroke-linejoin="round"/></svg>Financial Statements</li>
      <li><svg class="tick-icon" viewBox="0 0 20 20"><circle cx="9" cy="11" r="7" fill="none" stroke="var(--heading-blue)" stroke-width="2.2"/><path d="M5.5,10.5 L9,14 L18,4" fill="none" stroke="var(--heading-blue)" stroke-width="2.6" stroke-linecap="round" stroke-linejoin="round"/></svg>Partnership Taxation</li>
      <li><svg class="tick-icon" viewBox="0 0 20 20"><circle cx="9" cy="11" r="7" fill="none" stroke="var(--heading-blue)" stroke-width="2.2"/><path d="M5.5,10.5 L9,14 L18,4" fill="none" stroke="var(--heading-blue)" stroke-width="2.6" stroke-linecap="round" stroke-linejoin="round"/></svg>BAS preparation/lodgement</li>
      <li><svg class="tick-icon" viewBox="0 0 20 20"><circle cx="9" cy="11" r="7" fill="none" stroke="var(--heading-blue)" stroke-width="2.2"/><path d="M5.5,10.5 L9,14 L18,4" fill="none" stroke="var(--heading-blue)" stroke-width="2.6" stroke-linecap="round" stroke-linejoin="round"/></svg>Capital Gains Tax</li>
      <li><svg class="tick-icon" viewBox="0 0 20 20"><circle cx="9" cy="11" r="7" fill="none" stroke="var(--heading-blue)" stroke-width="2.2"/><path d="M5.5,10.5 L9,14 L18,4" fill="none" stroke="var(--heading-blue)" stroke-width="2.6" stroke-linecap="round" stroke-linejoin="round"/></svg>Business Start Ups</li>
      <li><svg class="tick-icon" viewBox="0 0 20 20"><circle cx="9" cy="11" r="7" fill="none" stroke="var(--heading-blue)" stroke-width="2.2"/><path d="M5.5,10.5 L9,14 L18,4" fill="none" stroke="var(--heading-blue)" stroke-width="2.6" stroke-linecap="round" stroke-linejoin="round"/></svg>Business Structuring</li>
      <li><svg class="tick-icon" viewBox="0 0 20 20"><circle cx="9" cy="11" r="7" fill="none" stroke="var(--heading-blue)" stroke-width="2.2"/><path d="M5.5,10.5 L9,14 L18,4" fill="none" stroke="var(--heading-blue)" stroke-width="2.6" stroke-linecap="round" stroke-linejoin="round"/></svg>Tax Planning</li>
    </ul>

    <div class="partner-badge" role="img" aria-label="Professional accreditation badge"></div>
    <div class="partner-dot" role="img" aria-label="Accounting software partner badge"></div>
  </div>
</body>
</html>
```